We need a logo design that explain all the products we possess.
The main goal is to represent graphically all the logos, pointing to one single logo - Voltane.
The descriptions are in french.
I have uploaded a file with 4 logos to use:
Voltane (the logo that all the rest should be pointing to)
RDM
Parcelin
PattouMou
All logo must be used in the vector graphic format, the description file is in each folder, it's the description that should be next to the logo.

The main goal of this is to create a banner 10' x 11' (estimated)

Target Market(s)

Cities

Requirements
Must have
• All the logos in the zip file in vector graphic.
Nice to have
• A background
Should not have
• Do not use TOB logo, it's a mix with RDM, and Tob Blue/dark blue with inscription "RDM", Charging fees for a part of the picture is not ok!

```html
<!DOCTYPE html>
<html lang="fr">
<head>
<meta charset="utf-8">
<title>Portail Voltanes 2.0</title>
<link href="https://fonts.googleapis.com/css2?family=Roboto:wght@700;900&display=swap" rel="stylesheet">
<style>
  :root {
    --sky: #29a8e0;
    --navy: #2a62ad;
    --green: #16a54e;
    --brand-blue: #1d74bb;
    --ink: #111111;
    --paper: #ffffff;
  }
  html, body {
    margin: 0;
    padding: 0;
    overflow: hidden;
    background: var(--paper);
  }
  .canvas {
    position: relative;
    width: 1200px;
    height: 1200px;
    overflow: hidden;
    background: var(--paper);
    font-family: "Roboto", Arial, sans-serif;
  }
  .network {
    position: absolute;
    inset: 0;
    width: 1200px;
    height: 1200px;
  }
  .hub-name,
  .hub-tagline,
  .product-mark,
  .product-label {
    position: absolute;
    margin: 0;
    text-align: center;
    transform: translateX(-50%);
    white-space: nowrap;
  }
  .hub-name {
    left: 626px;
    top: 425px;
    font-size: 64px;
    font-weight: 900;
    letter-spacing: 2px;
    color: var(--brand-blue);
    line-height: 1;
  }
  .hub-tagline {
    left: 623px;
    top: 491px;
    font-size: 19px;
    font-weight: 700;
    color: var(--ink);
  }
  .product-mark {
    font-weight: 900;
    line-height: 1;
  }
  .product-mark--rdm {
    left: 414px;
    top: 856px;
    font-size: 38px;
    color: var(--brand-blue);
  }
  .product-mark--parcelin {
    left: 626px;
    top: 958px;
    font-size: 20px;
    letter-spacing: 3px;
    color: var(--navy);
  }
  .product-mark--pattoumou {
    left: 840px;
    top: 861px;
    font-size: 24px;
    color: var(--sky);
  }
  .product-label {
    font-size: 16px;
    font-weight: 700;
    color: var(--ink);
    line-height: 19.5px;
  }
  .product-label--council { left: 413px; top: 988px; }
  .product-label--animals { left: 846px; top: 988px; }
  .product-label--land { left: 622px; top: 1078px; }
</style>
</head>
<body>
<main class="canvas">
  <svg class="network" viewBox="0 0 1500 1500" aria-hidden="true">
    <g class="hub-rings" fill="none" stroke-width="7" stroke-linecap="round">
      <path class="ring ring--sky" stroke="var(--sky)" d="M652,732 A297,297 0 1 1 903,742 L970,905"/>
      <path class="ring ring--navy" stroke="var(--navy)" d="M503,465 A282,282 0 1 1 783,747 L783,998"/>
      <path class="ring ring--green" stroke="var(--green)" d="M652,237 A265,265 0 1 1 680,712 L598,905"/>
    </g>
    <g class="connector-ends" fill="var(--paper)" stroke-width="7">
      <circle cx="588" cy="925" r="13" stroke="var(--green)"/>
      <circle cx="783" cy="1010" r="13" stroke="var(--navy)"/>
      <circle cx="978" cy="925" r="13" stroke="var(--sky)"/>
    </g>
    <g class="product-rings" fill="var(--paper)" stroke-width="37">
      <circle cx="517" cy="1093" r="102" stroke="var(--green)"/>
      <circle cx="783" cy="1212" r="102" stroke="var(--navy)"/>
      <circle cx="1050" cy="1093" r="102" stroke="var(--sky)"/>
    </g>
  </svg>

  <h1 class="hub-name">VOLTANES</h1>
  <p class="hub-tagline">PORTAIL VOLTANES 2.0</p>

  <p class="product-mark product-mark--rdm">RDM</p>
  <p class="product-mark product-mark--parcelin">PARCELIN</p>
  <p class="product-mark product-mark--pattoumou">PattouMou</p>

  <p class="product-label product-label--council">CONSEIL SANS PAPIER</p>
  <p class="product-label product-label--animals">LICENCES POUR ANIMAUX</p>
  <p class="product-label product-label--land">PERMIS<br>CARTE<br>INVENTAIRE<br>TAXES</p>
</main>
</body>
</html>
```